Website Design Project for Beauty & Wellness Professionals

As background information, I have a website that is focused on Beauty & Wellness Professionals:
- Job Search (www.trilhavelora.com)
- Business Classifieds (negocios.trilhavelora.com)
- Freelancer Classifieds (freelancer.trilhavelora.com)
- Course Reviews (cursos.trilhavelora.com)

All those websites use standard templates.

I need a DESIGN for the HOME PAGE (no coding) of the Website Platform that consolidates the four platforms under the same design.

Website designs that we like:
- quovenda.com
- mirtelpeek.com

Target Market(s)

Brazilian Professionals from Beauty & Wellness sector

Industry/Entity Type

Business

Requirements
Must have
• Website designs that we like:
- quovenda.com
- mirtelpeek.com

```html
<!DOCTYPE html>
<html lang="pt-BR">
<head>
<meta charset="utf-8">
<title>Trilha Velora – Home</title>
<link href="https://fonts.googleapis.com/css2?family=Open+Sans:ital,wght@0,400;0,600;0,700;1,700&display=swap" rel="stylesheet">
<style>
:root{
  --brand-orange:#f26b4a;
  --footer-salmon:#f4896b;
  --green:#4aa04a;
  --green-dark:#3a8a3a;
  --teal:#3fb6d3;
  --page-gray:#e9e9e9;
  --card-white:#ffffff;
  --ink:#333333;
  --muted:#888888;
  --line:#dddddd;
  --hero-dark:#3a2430;
}
*{box-sizing:border-box;margin:0;padding:0}
html,body{width:748px;height:1200px;overflow:hidden}
body{font-family:"Open Sans",Arial,sans-serif;color:var(--ink);background:var(--page-gray);font-size:8px;position:relative}

/* header */
.site-header{position:absolute;top:0;left:0;width:748px;height:44px;background:#fff;border-bottom:1px solid var(--line)}
.brand{position:absolute;left:28px;top:12px;display:flex;align-items:center;gap:6px;font-size:15px;font-weight:600;color:var(--brand-orange)}
.brand-mark{width:16px;height:16px;border-radius:50%;background:var(--brand-orange)}
.account-links{position:absolute;right:26px;top:3px;font-size:6px;color:var(--muted)}
.main-nav{position:absolute;right:24px;top:16px;display:flex;font-size:8px;font-weight:600}
.main-nav a{color:var(--ink);text-decoration:none;padding:6px 9px;border-left:1px solid var(--line)}
.main-nav a:first-child{border-left:0}
.main-nav a.is-active{color:var(--brand-orange)}

/* hero */
.hero{position:absolute;top:44px;left:0;width:748px;height:80px;background:linear-gradient(90deg,#5b2d3a,#8a4a58 30%,#b67f88 55%,#4b3440 80%,#2a1e26)}
.hero-title{position:absolute;top:10px;left:0;width:100%;text-align:center;color:#fff;font-weight:700;font-style:italic;font-size:18px}
.hero-sub{position:absolute;top:33px;left:0;width:100%;text-align:center;color:#f3dfe3;font-size:9px;font-style:italic}
.search-bar{position:absolute;top:52px;left:120px;width:508px;height:18px;display:flex;gap:3px}
.search-label{background:#333;color:#fff;font-weight:700;font-size:7px;padding:0 7px;display:flex;align-items:center}
.search-input{flex:1;background:#fff;border:1px solid #ccc}
.search-select{width:150px;background:#fff;border:1px solid #ccc;font-size:6px;color:var(--muted);padding:4px}
.search-button{width:56px;background:var(--green);color:#fff;font-weight:700;font-size:7px;display:flex;align-items:center;justify-content:center}

/* sidebar */
.sidebar{position:absolute;top:140px;left:28px;width:100px}
.side-heading{background:var(--green);color:#fff;font-weight:700;font-size:6.5px;padding:4px 5px;margin-bottom:6px}
.subscribe-box{background:var(--green);padding:5px;margin-bottom:10px}
.subscribe-box h3{color:#fff;font-size:6px;font-weight:700;margin-bottom:2px}
.subscribe-box p{color:#e3f3e3;font-size:5px;margin-bottom:4px}
.subscribe-row{display:flex;gap:2px}
.subscribe-row span{flex:1;height:10px;background:#fff}
.subscribe-row b{background:var(--green-dark);color:#fff;font-size:5px;padding:2px 3px}
.side-block{background:#fff;margin-bottom:10px;padding:4px 5px;font-size:5px;color:var(--muted)}
.side-block h3{font-size:6px;font-weight:700;color:var(--ink);margin-bottom:3px}
.side-block li{list-style:none;padding:2px 0;border-top:1px solid #eee;line-height:1.3}
.friends-grid{display:grid;grid-template-columns:repeat(5,1fr);gap:2px;margin-top:4px}
.friends-grid span{height:14px;background:#c9b3a8}
.friends-page{display:flex;gap:4px;align-items:center;margin-bottom:3px}
.friends-page span{width:14px;height:14px;background:var(--brand-orange)}

/* listings */
.listings{position:absolute;top:140px;left:133px;width:589px}
.tabs{display:flex;gap:2px;margin-bottom:6px}
.tabs span{background:var(--teal);color:#fff;font-weight:700;font-size:6px;padding:4px 10px}
.tabs span.is-current{background:var(--brand-orange)}
.listing{height:62px;background:var(--card-white);margin-bottom:4px;display:flex;padding:7px 8px;gap:10px;border:1px solid #e2e2e2}
.avatar{width:46px;height:46px;border-radius:50%;background:linear-gradient(135deg,#c9a58f,#6d5a52);flex:none}
.listing-body{width:300px}
.listing-name{font-weight:700;font-size:7px;margin-bottom:2px}
.listing-text{font-size:5px;color:var(--muted);line-height:1.35;margin-bottom:4px}
.listing-actions{display:flex;gap:3px}
.listing-actions span{background:var(--teal);color:#fff;font-size:5px;padding:2px 5px}
.listing-actions span.alt{background:#9fd6e6}

/* footer */
.site-footer{position:absolute;top:770px;left:0;width:748px;height:430px;background:var(--footer-salmon);color:#fff;text-align:center}
.social-row{display:flex;justify-content:center;gap:22px;margin-top:22px}
.social-row span{width:38px;height:38px;border-radius:50%;background:#fff;opacity:.9}
.footer-section{width:660px;margin:22px auto 0;font-size:5.5px;line-height:1.6;color:#fff6f2}
.footer-section h4{font-size:7px;font-weight:700;color:#fff;margin-bottom:3px}
.copyright{position:absolute;bottom:14px;left:0;width:100%;font-size:5.5px;color:#fff}
</style>
</head>
<body>

<header class="site-header">
  <div class="brand"><span class="brand-mark"></span>Trilha Velora</div>
  <div class="account-links">Welcome, Guest | Login | Register</div>
  <nav class="main-nav">
    <a class="is-active">Home</a>
    <a>Categories of Business ▾</a>
    <a>For Professionals</a>
    <a>For Business</a>
    <a>About Us</a>
  </nav>
</header>

<section class="hero" role="img" aria-label="Blurred photo of a beauty salon interior">
  <h1 class="hero-title">Neque porro quisquam est qui dolorem</h1>
  <p class="hero-sub">Neque porro quisquam est qui dolorem ipsum quia</p>
  <div class="search-bar">
    <span class="search-label">Local Job Search</span>
    <span class="search-input"></span>
    <span class="search-select">All categories ▾</span>
    <span class="search-button">SEARCH</span>
  </div>
</section>

<aside class="sidebar">
  <div class="side-heading">CATEGORIES ▾</div>
  <div class="subscribe-box">
    <h3>SUBSCRIBE TRILHA VELORA</h3>
    <p>Get new jobs in your inbox</p>
    <div class="subscribe-row"><span></span><b>SUBSCRIBE</b></div>
  </div>
  <div class="side-block">
    <h3>BEAUTY CAREER</h3>
    <ul>
      <li>Salon jobs near your city</li>
      <li>Spa and wellness openings</li>
      <li>Clinic roles for therapists</li>
      <li>New courses this month</li>
    </ul>
  </div>
  <div class="side-block">
    <h3>CORE BUSINESSES</h3>
    <ul>
      <li>Hair salon for sale – São Paulo, central area</li>
      <li>Nail studio with staff – Osasco, busy street</li>
      <li>Spa space to rent – Santos, near beach</li>
      <li>Barber shop chair – Campinas, new shop</li>
      <li>Esthetic clinic partner – Sorocaba, ready room</li>
      <li>Makeup studio share – Jundiaí, full kit</li>
    </ul>
  </div>
  <div class="side-block">
    <h3>REDE SOCIAL FRIENDS</h3>
    <div class="friends-page"><span></span>Trilha Velora</div>
    <div class="friends-grid" role="img" aria-label="Grid of friend profile photos">
      <span></span><span></span><span></span><span></span><span></span>
      <span></span><span></span><span></span><span></span><span></span>
    </div>
  </div>
</aside>

<main class="listings">
  <div class="tabs"><span class="is-current">RECENT</span><span>MOST VIEWED</span><span>FEATURED</span></div>

  <article class="listing"><div class="avatar" role="img" aria-label="Professional profile photo"></div><div class="listing-body"><p class="listing-name">Marina Coutelo Ravesi – São Paulo</p><p class="listing-text">Hair stylist with ten years in color and cuts, looking for a salon with steady clients and fair commission in the city.</p><div class="listing-actions"><span>View Profile</span><span class="alt">Contact</span><span class="alt">Save</span></div></div></article>

  <article class="listing"><div class="avatar" role="img" aria-label="Professional profile photo"></div><div class="listing-body"><p class="listing-name">Helena Brastino Quirel – Manicure / Pedicure</p><p class="listing-text">Manicure and pedicure expert, gel and art nails, available for part time work in studios and spas near the center.</p><div class="listing-actions"><span>View Profile</span><span class="alt">Contact</span><span class="alt">Save</span></div></div></article>

  <article class="listing"><div class="avatar" role="img" aria-label="Professional profile photo"></div><div class="listing-body"><p class="listing-name">Renata Olvides Paim – Eyebrow Designer – Osasco</p><p class="listing-text">Eyebrow designer with henna and lash lift training, seeking a clinic role with room to grow and learn new skills.</p><div class="listing-actions"><span>View Profile</span><span class="alt">Contact</span><span class="alt">Save</span></div></div></article>

  <article class="listing"><div class="avatar" role="img" aria-label="Professional profile photo"></div><div class="listing-body"><p class="listing-name">Marina Coutelo Ravesi – São Paulo</p><p class="listing-text">Hair stylist with ten years in color and cuts, looking for a salon with steady clients and fair commission in the city.</p><div class="listing-actions"><span>View Profile</span><span class="alt">Contact</span><span class="alt">Save</span></div></div></article>

  <article class="listing"><div class="avatar" role="img" aria-label="Professional profile photo"></div><div class="listing-body"><p class="listing-name">Helena Brastino Quirel – Manicure / Pedicure</p><p class="listing-text">Manicure and pedicure expert, gel and art nails, available for part time work in studios and spas near the center.</p><div class="listing-actions"><span>View Profile</span><span class="alt">Contact</span><span class="alt">Save</span></div></div></article>

  <article class="listing"><div class="avatar" role="img" aria-label="Professional profile photo"></div><div class="listing-body"><p class="listing-name">Renata Olvides Paim – Eyebrow Designer – Osasco</p><p class="listing-text">Eyebrow designer with henna and lash lift training, seeking a clinic role with room to grow and learn new skills.</p><div class="listing-actions"><span>View Profile</span><span class="alt">Contact</span><span class="alt">Save</span></div></div></article>

  <article class="listing"><div class="avatar" role="img" aria-label="Professional profile photo"></div><div class="listing-body"><p class="listing-name">Renata Olvides Paim – Eyebrow Designer – Osasco</p><p class="listing-text">Eyebrow designer with henna and lash lift training, seeking a clinic role with room to grow and learn new skills.</p><div class="listing-actions"><span>View Profile</span><span class="alt">Contact</span><span class="alt">Save</span></div></div></article>

  <article class="listing"><div class="avatar" role="img" aria-label="Professional profile photo"></div><div class="listing-body"><p class="listing-name">Marina Coutelo Ravesi – São Paulo</p><p class="listing-text">Hair stylist with ten years in color and cuts, looking for a salon with steady clients and fair commission in the city.</p><div class="listing-actions"><span>View Profile</span><span class="alt">Contact</span><span class="alt">Save</span></div></div></article>

  <article class="listing"><div class="avatar" role="img" aria-label="Professional profile photo"></div><div class="listing-body"><p class="listing-name">Helena Brastino Quirel – Manicure / Pedicure</p><p class="listing-text">Manicure and pedicure expert, gel and art nails, available for part time work in studios and spas near the center.</p><div class="listing-actions"><span>View Profile</span><span class="alt">Contact</span><span class="alt">Save</span></div></div></article>
</main>

<footer class="site-footer">
  <div class="social-row"><span></span><span></span><span></span><span></span></div>
  <section class="footer-section">
    <h4>JOB SEARCHES</h4>
    <p>Hair Stylist · Manicure · Esthetician · Massage Therapist · Makeup Artist · Barber · Eyebrow Designer · Receptionist · Salon Manager · Spa Therapist · Podiatrist · Depilator · Lash Designer · Nail Artist · Beauty Consultant · Cosmetologist</p>
  </section>
  <section class="footer-section">
    <h4>PROFESSIONALS</h4>
    <p>Hair Stylists in São Paulo · Manicures in Osasco · Estheticians in Santos · Massage Therapists in Campinas · Barbers in Sorocaba · Makeup Artists in Jundiaí · Lash Designers in Guarulhos</p>
  </section>
  <section class="footer-section">
    <h4>BEAUTY CAREER</h4>
    <p>www.trilhavelora.com · negocios.trilhavelora.com · freelancer.trilhavelora.com · cursos.trilhavelora.com</p>
  </section>
  <p class="copyright">© 2014 Trilha Velora. All rights reserved.</p>
</footer>

</body>
</html>
```